Business Card Design Project

I am looking for a classy business card design for a product design consultancy. We specialize in Product Design, Prototyping, and Manufacturing Consulting. Products that we design range from consumer electronics to household products all the way to sporting goods. We are based in Arizona and called "Pelican Forge Studio." We like to have fun and goof off as much as we like to create new products. We are young and energetic so we would like our business cards to reflect that. We already have a logo that we would like to implement into the card design. A plain rectangular business card is boring so feel free to get creative, but please, no avocado shaped cards (it's far too literal). Also feel free to play around with textured card stocks or plastic. The final design that we choose will pay attention to all of the little details. Our cards will need to be 2 sided. We're giving you guys free reign to design as you would like. Please have fun with this, it will reflect in our business card.

Thanks guys,
Pelican Forge Studio Team
Updates

Industry/Entity Type

Electronics

Requirements
Must have
• We would like to have a spot UV coating somewhere on the business card design if possible.
Nice to have
• Let's see some designs with custom shapes rather than typical rectangular business cards but please no avocado shaped cards, thanks. Also play around with textured card socks.

Files

```html
<!DOCTYPE html>
<html lang="en">
<head>
<meta charset="utf-8">
<title>Pelican Forge Studio – Business Card</title>
<link rel="stylesheet" href="https://fonts.googleapis.com/css2?family=Nunito+Sans:wght@300;400&display=swap">
<style>
  :root {
    --backdrop: #2b2b2b;
    --card-white: #f4f4f4;
    --brand-green: #94bf2e;
    --brand-green-dark: #7fa82a;
    --spot-uv: #a9cd52;
    --ink-grey: #6b6b6b;
    --ink-dark: #555555;
  }
  * { box-sizing: border-box; margin: 0; padding: 0; }
  html, body {
    width: 1200px;
    height: 900px;
    overflow: hidden;
    background: var(--backdrop);
    font-family: "Nunito Sans", sans-serif;
  }
  .sheet {
    position: relative;
    width: 1200px;
    height: 900px;
    display: flex;
    align-items: center;
    justify-content: center;
    gap: 40px;
  }
  .card {
    position: relative;
    width: 540px;
    height: 309px;
    border-radius: 4px;
    overflow: hidden;
  }
  /* Back side: white with contact details */
  .card--back {
    background: var(--card-white);
    padding: 40px 44px;
  }
  .wordmark {
    display: flex;
    align-items: center;
    gap: 12px;
  }
  .wordmark__dot {
    width: 34px;
    height: 34px;
    border-radius: 50%;
    background: var(--brand-green);
    flex: none;
  }
  .wordmark__name {
    font-weight: 400;
    font-size: 34px;
    letter-spacing: 0.5px;
    color: var(--brand-green);
    white-space: nowrap;
  }
  .contact {
    margin-top: 28px;
    color: var(--ink-grey);
    font-weight: 300;
  }
  .contact__name {
    font-size: 19px;
    font-weight: 400;
    color: var(--ink-dark);
    letter-spacing: 0.5px;
  }
  .contact__title {
    font-size: 14px;
    margin-bottom: 14px;
  }
  .contact__line {
    font-size: 14px;
    line-height: 1.45;
  }
  .contact__label {
    display: inline-block;
    width: 16px;
    color: var(--brand-green);
  }
  .contact__web { margin-top: 10px; }
  .contact__web .accent { color: var(--brand-green); }
  /* Front side: green with spot UV name */
  .card--front {
    background: var(--brand-green);
    display: flex;
    align-items: center;
    justify-content: center;
  }
  .spot-uv {
    display: flex;
    align-items: center;
    gap: 14px;
  }
  .spot-uv__dot {
    width: 44px;
    height: 44px;
    border-radius: 50%;
    background: var(--spot-uv);
    flex: none;
  }
  .spot-uv__name {
    font-weight: 400;
    font-size: 40px;
    color: var(--spot-uv);
    letter-spacing: 0.5px;
    white-space: nowrap;
  }
</style>
</head>
<body>
<main class="sheet">
  <section class="card card--back" aria-label="Card back">
    <div class="wordmark">
      <span class="wordmark__dot"></span>
      <span class="wordmark__name">Pelican Forge Studio</span>
    </div>
    <div class="contact">
      <p class="contact__name">DANA WHITFIELD</p>
      <p class="contact__title">President</p>
      <p class="contact__line"><span class="contact__label">T</span>480.555.0142</p>
      <p class="contact__line"><span class="contact__label">M</span>602.555.0187</p>
      <p class="contact__line">dana@pelicanforgestudio.com</p>
      <p class="contact__line contact__web">www.<span class="accent">pelican</span>forgestudio.com</p>
    </div>
  </section>
  <section class="card card--front" aria-label="Card front">
    <div class="spot-uv">
      <span class="spot-uv__dot"></span>
      <span class="spot-uv__name">Pelican Forge Studio</span>
    </div>
  </section>
</main>
</body>
</html>
```